"The Wandering Mentor", a Higher Ed blogger, would like a wordpress design

I would like a wordpress design for blogs written by "The Wandering Mentor." that can be easily expanded by me once the initial design is complete.

Here is context which I would like included on the Home/Welcome page: "I started The Wandering Mentor in 2021 to write about the practice of academic advising through the lens of horsemanship. After one year of developing skills as a brand new equestrian, I couldn’t help but notice the similarities between my vocation as an academic advisor and my avocation as a budding equestrian. I hope my musings about my journey in two very different fields will cultivate curiosity, widen your aperture and ignite academic advisors to take their practice to the next level. "

The wordpress will primarily have blogs by myself or guest bloggers writing about academic advising for advisors, but I may widen my audience to include students and families. I'd like to have readers submit questions that I can answer. Depending on interest, I may want to have a section on Horsemanship but that is not truly the focus of this site.

I'd like the feel of the site to be positive, fresh, modern (but not too wild), with the emphasis on Higher Ed/Academic Advising as opposed to equestrian pursuits. I don't want it to feel clunky and blocky like some sites that have to do with education. I'm hoping that readers will have some "aha" moments after reading some of the posts.

I have included my logo files

```html
<!DOCTYPE html>
<html lang="en">
<head>
<meta charset="utf-8">
<title>The Wandering Mentor — Home</title>
<link href="https://fonts.googleapis.com/css2?family=Playfair+Display:wght@700;900&family=Montserrat:wght@400;500;600;700&display=swap" rel="stylesheet">
<style>
:root{
  --gold:#d2a961;
  --gold-soft:#f3e9d6;
  --ink:#141414;
  --dark:#1d1d1d;
  --text:#555;
  --hero-bg:#efefef;
  --canvas:#f7f6f3;
  --white:#fff;
}
*{box-sizing:border-box;margin:0;padding:0}
html,body{width:1200px;height:3995px;overflow:hidden;background:var(--canvas)}
body{font-family:"Montserrat",sans-serif;color:var(--text)}
.page{position:absolute;left:100px;top:44px;width:1000px;height:3907px;background:var(--white);box-shadow:0 10px 40px rgba(0,0,0,.08);overflow:hidden}
.abs{position:absolute}
.title{font-family:"Playfair Display",serif;font-weight:900;color:var(--ink);text-transform:uppercase;line-height:1.02;letter-spacing:.5px}
.copy{font-size:11px;line-height:1.75;color:var(--text)}
.learn{font-size:10px;font-weight:600;color:var(--ink);display:flex;align-items:center;gap:8px}
.learn::before{content:"";width:18px;height:1.5px;background:var(--ink)}
.photo{position:absolute}
.date{position:absolute;right:0;bottom:0;background:var(--gold);color:#fff;font-size:8px;font-weight:600;padding:5px 12px;letter-spacing:.5px}
.author{display:flex;align-items:center;gap:14px}
.avatar{width:38px;height:38px;border-radius:50%;background:#e6e1da}
.author b{display:block;font-size:9px;letter-spacing:2px;color:var(--gold);font-weight:600}
.author span{font-size:8px;color:#aaa}
.circle-btn{position:absolute;width:26px;height:26px;border-radius:50%;background:#fff;border:1px solid #ddd;display:flex;align-items:center;justify-content:center;z-index:2}
.social{position:absolute;width:24px;height:24px;border-radius:50%;border:1px solid #ccc;background:#fff}
.brand{display:flex;align-items:center;gap:10px;font-family:"Playfair Display",serif;font-weight:700;font-size:14px;letter-spacing:2px;text-transform:uppercase;color:var(--gold)}
.brand i{width:12px;height:12px;border-radius:50%;background:var(--gold);display:block}
/* hero */
.hero{position:absolute;left:0;top:0;width:1000px;height:573px}
.hero-panel{position:absolute;left:0;top:0;width:483px;height:573px;background:linear-gradient(135deg,#f6f6f6,#e9e9e9)}
.hero-letter{position:absolute;left:470px;top:90px;font-family:"Playfair Display",serif;font-weight:900;font-size:340px;color:var(--gold-soft);line-height:1}
.hero-caption{position:absolute;left:582px;top:436px;width:220px;z-index:2}
.btn{background:var(--gold);color:var(--ink);font-size:10px;font-weight:600;display:flex;align-items:center;justify-content:center}
.menu{position:absolute;left:860px;top:48px;width:36px;z-index:2}
.menu span{display:block;height:3px;background:var(--ink);margin-bottom:5px;margin-left:auto}
/* subscribe */
.subscribe{position:absolute;left:0;top:1766px;width:1000px;height:268px;background:var(--gold);text-align:center}
.field{position:absolute;left:307px;top:179px;width:386px;height:34px;background:#fff;display:flex}
.field span{flex:1;font-size:9px;color:#666;text-align:left;padding:11px 18px}
.field b{width:118px;margin:3px;background:var(--gold);font-size:9px;font-weight:600;color:var(--ink);display:flex;align-items:center;justify-content:center}
/* form */
.ask{position:absolute;left:105px;top:2896px;width:253px;height:315px;background:var(--dark);padding:28px 22px}
.ask h3{color:#fff;font-size:17px;font-weight:500;margin-bottom:18px}
.ask .in{background:#fff;height:28px;margin-bottom:6px;font-size:8px;color:#999;padding:10px}
.ask .ta{background:#fff;height:96px;font-size:8px;color:#999;padding:10px}
.ask .send{margin-top:16px;border:1px solid var(--gold);height:26px;color:#fff;font-size:8px;font-weight:700;letter-spacing:2px;display:flex;align-items:center;justify-content:center}
/* footer */
.footer{position:absolute;left:0;top:3482px;width:1000px;height:373px;background:var(--dark);text-align:center}
.bar{position:absolute;left:0;top:3855px;width:1000px;height:52px;background:var(--gold);font-size:10px;color:var(--ink);display:flex;align-items:center;justify-content:center;font-weight:500}
</style>
</head>
<body>
<main class="page">

  <section class="hero">
    <div class="hero-panel"></div>
    <div class="hero-letter" aria-hidden="true">W</div>
    <div class="abs brand" style="left:105px;top:62px">The Wandering Mentor<i></i></div>
    <h1 class="abs title" style="left:105px;top:190px;font-size:50px">Wandering<br>Academic<br>Advisor</h1>
    <p class="abs copy" style="left:105px;top:378px;width:330px">I write about the practice of academic advising through the lens of horsemanship, to widen your aperture.</p>
    <div class="abs btn" style="left:105px;top:554px;width:146px;height:30px">Subscribe Us</div>
    <div class="photo" role="img" aria-label="Dark-maned horse in falling snow, head and mane" style="left:600px;top:80px;width:400px;height:340px;background:linear-gradient(160deg,#6b5848,#2a211b 55%,#3b3029)"></div>
    <div class="photo" role="img" aria-label="Neck of the dark horse in snow" style="left:830px;top:420px;width:170px;height:153px;background:linear-gradient(180deg,#3b3029,#1e1813)"></div>
    <div class="menu"><span style="width:36px"></span><span style="width:26px"></span><span style="width:36px"></span></div>
    <div class="hero-caption">
      <h4 style="font-size:9px;font-weight:700;color:var(--ink);margin-bottom:6px">LOREM IPSUM IS SIMPLY</h4>
      <p class="copy" style="font-size:9px">Lorem Ipsum is simply dummy text of the printing and typesetting industry. Lorem Ipsum has been the industry standard.</p>
      <div class="learn" style="margin-top:8px;font-size:8px">Learn more</div>
    </div>
    <div class="circle-btn" style="left:470px;top:484px"><svg width="8" height="8" viewBox="0 0 8 8"><path d="M2 1l4 3-4 3" fill="none" stroke="#222" stroke-width="1.2"/></svg></div>
    <div class="circle-btn" style="left:470px;top:518px"><svg width="8" height="8" viewBox="0 0 8 8"><path d="M6 1L2 4l4 3" fill="none" stroke="#222" stroke-width="1.2"/></svg></div>
    <div class="social" style="left:845px;top:537px"></div>
    <div class="social" style="left:878px;top:537px"></div>
    <div class="social" style="left:911px;top:537px"></div>
  </section>

  <section class="posts">
    <div class="photo" role="img" aria-label="Galloping horses in black and white" style="left:105px;top:671px;width:453px;height:373px;background:radial-gradient(circle at 50% 55%,#8a8a8a,#1e1e1e 65%,#0a0a0a)"><span class="date">15-SEP-2021</span></div>
    <h2 class="abs title" style="left:596px;top:668px;font-size:42px">Academic<br>Advisor</h2>
    <p class="abs copy" style="left:596px;top:780px;width:310px">Lorem Ipsum is simply dummy text of the printing and typesetting industry. Lorem Ipsum has been the industry's standard dummy text ever since the 1500s.</p>
    <div class="abs author" style="left:605px;top:874px"><div class="avatar"></div><div><b>JOHN DOE</b><span>Writer</span></div></div>

    <div class="photo" role="img" aria-label="Rider on horseback on a sunlit forest trail" style="left:577px;top:950px;width:321px;height:347px;background:linear-gradient(180deg,#c9b27a,#8a6a34 50%,#3f3820)"><span class="date">15-SEP-2021</span></div>
    <h3 class="abs title" style="left:105px;top:1083px;font-size:28px">Lorem Ipsum is a<br>Dummy</h3>
    <p class="abs copy" style="left:105px;top:1172px;width:380px">Lorem Ipsum is simply dummy text of the printing and typesetting industry. Lorem Ipsum has been the industry's standard dummy text ever since the 1500s.</p>
    <div class="abs learn" style="left:105px;top:1252px">Learn more</div>

    <div class="photo" role="img" aria-label="Rider jumping a chestnut horse" style="left:105px;top:1303px;width:453px;height:374px;background:linear-gradient(160deg,#e4e6e8,#b6a08a 45%,#7a3e1c)"><span class="date">15-SEP-2021</span></div>
    <h3 class="abs title" style="left:596px;top:1328px;font-size:28px">Lorem Ipsum is<br>a Dummy</h3>
    <p class="abs copy" style="left:596px;top:1416px;width:300px">Lorem Ipsum is simply dummy text of the printing and typesetting industry. Lorem Ipsum has been the industry's standard dummy text ever since the 1500s.</p>
    <div class="abs learn" style="left:596px;top:1500px">Learn more</div>
    <div class="photo" role="img" aria-label="Rider on a snowy path" style="left:577px;top:1557px;width:117px;height:122px;background:linear-gradient(180deg,#e8e9ea,#a8a9ab)"></div>
    <div class="abs" style="left:711px;top:1562px;width:190px">
      <h4 style="font-size:9px;font-weight:700;color:var(--ink);margin-bottom:6px">LOREM IPSUM IS SIMPLY</h4>
      <p class="copy" style="font-size:9px">Lorem Ipsum is simply dummy text of the printing and typesetting industry since the 1500s.</p>
      <div class="learn" style="margin-top:8px;font-size:8px">Learn more</div>
    </div>
  </section>

  <section class="subscribe">
    <h2 class="title" style="font-size:27px;padding-top:64px">Subscribe to get updates!</h2>
    <p class="copy" style="color:var(--ink);width:360px;margin:14px auto 0">Lorem Ipsum is simply dummy text of the printing and typesetting industry. Lorem Ipsum has been the industry's standard dummy text ever since the 1500s.</p>
    <div class="field"><span>Email Address</span><b>Subscribe Us</b></div>
  </section>

  <section class="budding">
    <h2 class="abs title" style="left:105px;top:2112px;font-size:42px">Budding<br>Equestrian</h2>
    <p class="abs copy" style="left:105px;top:2224px;width:500px">Lorem Ipsum is simply dummy text of the printing and typesetting industry. Lorem Ipsum has been the industry's standard dummy text ever since the 1500s.</p>
    <div class="abs author" style="left:105px;top:2290px"><div class="avatar"></div><div><b>JOHN DOE</b><span>Writer</span></div></div>
    <div class="abs learn" style="left:105px;top:2384px">Learn more</div>
    <div class="photo" role="img" aria-label="Horse in a stable" style="left:369px;top:2290px;width:117px;height:107px;background:linear-gradient(160deg,#7a6552,#2c2420)"></div>
    <div class="photo" role="img" aria-label="Rider with a horse" style="left:505px;top:2290px;width:117px;height:107px;background:linear-gradient(160deg,#d8d4cf,#4a3a30 60%,#b52a2a)"></div>
    <div class="circle-btn" style="left:356px;top:2316px"><svg width="8" height="8" viewBox="0 0 8 8"><path d="M2 1l4 3-4 3" fill="none" stroke="#222" stroke-width="1.2"/></svg></div>
    <div class="circle-btn" style="left:356px;top:2350px"><svg width="8" height="8" viewBox="0 0 8 8"><path d="M6 1L2 4l4 3" fill="none" stroke="#222" stroke-width="1.2"/></svg></div>
    <div class="photo" role="img" aria-label="Close-up of horses' heads with bridles" style="left:646px;top:2117px;width:252px;height:280px;background:linear-gradient(135deg,#3b2a4a,#7b4a3a 50%,#d6b48a)"><span class="date">15-SEP-2021</span></div>

    <div class="photo" role="img" aria-label="Leather saddle on a blue pad" style="left:105px;top:2437px;width:453px;height:290px;background:linear-gradient(150deg,#2d3a4c,#6b3c1e 50%,#2a3346)"><span class="date">15-SEP-2021</span></div>
    <h3 class="abs title" style="left:596px;top:2437px;font-size:28px">Lorem Ipsum is<br>a Dummy</h3>
    <p class="abs copy" style="left:596px;top:2524px;width:300px">Lorem Ipsum is simply dummy text of the printing and typesetting industry. Lorem Ipsum has been the industry's standard dummy text ever since the 1500s.</p>
    <div class="abs learn" style="left:596px;top:2608px">Learn more</div>
    <div class="abs author" style="left:605px;top:2660px"><div class="avatar"></div><div><b>JOHN DOE</b><span>Writer</span></div></div>
  </section>

  <section class="horsemanship">
    <h2 class="abs title" style="left:105px;top:2808px;font-size:40px">Horsemanship</h2>
    <form class="ask">
      <h3>How can I help you</h3>
      <div class="in">Name</div>
      <div class="ta">Type your question</div>
      <div class="send">SEND</div>
    </form>
    <div class="photo" role="img" aria-label="Riders before a green mountain and purple flowers" style="left:105px;top:3231px;width:253px;height:168px;background:linear-gradient(180deg,#9cc0e0,#5d8a4a 55%,#7a6ab0)"></div>
    <div class="photo" role="img" aria-label="Horse hooves in dust at dusk" style="left:373px;top:2896px;width:522px;height:505px;background:linear-gradient(170deg,#3a2c22,#1a1410 55%,#5a4430)"></div>
    <h3 class="abs title" style="left:405px;top:3275px;font-size:28px;color:#fff">Lorem Ipsum is</h3>
    <p class="abs copy" style="left:405px;top:3318px;width:400px;color:#ddd">Lorem Ipsum is simply dummy text of the printing and typesetting industry. Lorem Ipsum has been the industry's standard dummy text ever since the 1500s.</p>
  </section>

  <footer class="footer">
    <div class="brand" style="justify-content:center;padding-top:96px;font-size:20px">The Wandering Mentor<i></i></div>
    <p class="copy" style="color:#ccc;width:520px;margin:88px auto 0">Lorem Ipsum is simply dummy text of the printing and typesetting industry. Lorem Ipsum has been the industry's standard dummy text ever since the 1500s.</p>
    <div class="social" style="left:442px;top:285px;background:none;border-color:var(--gold)"></div>
    <div class="social" style="left:488px;top:285px;background:none;border-color:var(--gold)"></div>
    <div class="social" style="left:534px;top:285px;background:none;border-color:var(--gold)"></div>
  </footer>
  <div class="bar">© 2021 The Wandering Mentor. All rights reserved.</div>

</main>
</body>
</html>
```